Jolly Paws Business Card Update

I have a business card which I love. I want to keep the same logo, colours, font and style. I want to upgrade the scripting and remove some elements and add others.
On the front side under Services - remove the existing wording and insert - Providing individual coaching strategies to create happy, healthy and social canine companions
Under Rebecca Thornley amend the current wording to read: Qualified in Dog Behavioural Training, Natural Animal Healthcare and Animal Health Science
On the reverse side to remove the web address.

```html
<!DOCTYPE html>
<html lang="en">
<head>
<meta charset="utf-8">
<title>Jolly Paws Business Card</title>
<link rel="stylesheet" href="https://fonts.googleapis.com/css2?family=Archivo:wght@400;700&display=swap">
<style>
  :root {
    --backdrop: #c9c9c9;
    --sky-top: #29d3ff;
    --sky-mid: #1f9bff;
    --sky-deep: #0022ff;
    --red-edge: #4a0006;
    --red-core: #ff0000;
    --cream: #f2efc4;
    --ink: #111111;
    --white: #ffffff;
  }
  html, body {
    margin: 0;
    padding: 0;
    width: 1200px;
    height: 846px;
    overflow: hidden;
    background: var(--backdrop);
    font-family: "Archivo", Arial, sans-serif;
  }
  .sheet {
    position: relative;
    width: 1200px;
    height: 846px;
  }
  .card {
    position: absolute;
    left: 331px;
    width: 538px;
    height: 332px;
    display: block;
  }
  .card--front { top: 71px; }
  .card--back { top: 446px; }
  .services-title { font-weight: 700; font-size: 16px; fill: var(--white); }
  .services-copy { font-weight: 400; font-size: 16.5px; fill: var(--white); }
  .ribbon-text { font-weight: 400; font-size: 13.5px; fill: var(--ink); }
  .holder-name { font-weight: 700; font-size: 16px; fill: var(--white); letter-spacing: -0.3px; }
  .contact { font-weight: 400; font-size: 16px; fill: var(--white); }
  .credentials { font-weight: 400; font-size: 11px; fill: var(--white); letter-spacing: -0.2px; }
  .brand-name { font-weight: 700; fill: var(--cream); }
  .tagline { font-weight: 400; font-size: 17px; fill: var(--white); }
</style>
</head>
<body>
<main class="sheet">

  <!-- Front of card -->
  <svg class="card card--front" viewBox="0 0 538 332" xmlns="http://www.w3.org/2000/svg" role="group" aria-label="Jolly Paws card, front">
    <defs>
      <linearGradient id="front-sky" x1="0" y1="0" x2="0" y2="1">
        <stop offset="0" stop-color="var(--sky-top)"/>
        <stop offset="0.15" stop-color="var(--sky-top)"/>
        <stop offset="0.45" stop-color="var(--sky-mid)"/>
        <stop offset="0.8" stop-color="var(--sky-deep)"/>
      </linearGradient>
      <linearGradient id="front-red" x1="0" y1="0" x2="1" y2="0">
        <stop offset="0" stop-color="var(--red-edge)"/>
        <stop offset="0.5" stop-color="var(--red-core)"/>
        <stop offset="1" stop-color="var(--red-edge)"/>
      </linearGradient>
      <path id="ribbon-line" d="M0,243 Q269,190 538,240"/>
    </defs>

    <rect class="card-sky" width="538" height="332" fill="url(#front-sky)"/>
    <path class="card-red-base" d="M0,246 Q269,194 538,244 L538,332 L0,332 Z" fill="url(#front-red)"/>
    <path class="ribbon" d="M0,227 Q269,176.5 538,224 L538,246 Q269,195 0,248 Z" fill="var(--cream)"/>
    <text class="ribbon-text"><textPath href="#ribbon-line" startOffset="50%" text-anchor="middle" textLength="478" lengthAdjust="spacingAndGlyphs">promoting communication and connection between dogs and their families</textPath></text>

    <g class="brand-mark">
      <circle cx="149" cy="106" r="58" fill="var(--red-edge)"/>
      <text class="brand-name" x="149" y="112" font-size="17" text-anchor="middle">Jolly Paws</text>
    </g>

    <line class="divider" x1="231" y1="56" x2="231" y2="154" stroke="var(--white)" stroke-width="1.2"/>

    <text class="services-title" x="255" y="69">SERVICES</text>
    <text class="services-copy" x="255" y="99">
      <tspan x="255">Providing individual</tspan>
      <tspan x="255" dy="18.2">coaching strategies to</tspan>
      <tspan x="255" dy="18.2">create happy, healthy and</tspan>
      <tspan x="255" dy="18.2">social canine companions</tspan>
    </text>

    <text class="holder-name" x="268" y="259" text-anchor="middle">Rebecca Thornley</text>

    <g class="contact-row">
      <g class="icon-phone">
        <circle cx="111" cy="276" r="8" fill="none" stroke="var(--white)" stroke-width="1.4"/>
        <rect x="107.5" y="270.5" width="7" height="11" rx="1.2" fill="var(--white)"/>
        <rect x="108.8" y="272" width="4.4" height="5" fill="var(--red-edge)"/>
      </g>
      <text class="contact" x="124" y="282">0412 807265</text>
      <g class="icon-mail">
        <circle cx="242" cy="276" r="8" fill="none" stroke="var(--white)" stroke-width="1.4"/>
        <rect x="237" y="272.5" width="10" height="7" rx="1" fill="var(--white)"/>
        <path d="M237.5,273 L242,277 L246.5,273" fill="none" stroke="var(--red-core)" stroke-width="1"/>
      </g>
      <text class="contact" x="255" y="282">jollypaws.coach@mail.com</text>
    </g>

    <text class="credentials" x="268" y="309" text-anchor="middle">Qualified in Dog Behavioural Training, Natural Animal Healthcare and Animal Health Science</text>
  </svg>

  <!-- Back of card -->
  <svg class="card card--back" viewBox="0 0 538 332" xmlns="http://www.w3.org/2000/svg" role="group" aria-label="Jolly Paws card, back">
    <defs>
      <linearGradient id="back-sky" x1="0" y1="0" x2="0" y2="1">
        <stop offset="0" stop-color="var(--sky-top)"/>
        <stop offset="0.15" stop-color="var(--sky-top)"/>
        <stop offset="0.5" stop-color="var(--sky-mid)"/>
        <stop offset="0.88" stop-color="var(--sky-deep)"/>
      </linearGradient>
      <linearGradient id="back-red" x1="0" y1="0" x2="1" y2="0">
        <stop offset="0" stop-color="var(--red-edge)"/>
        <stop offset="0.5" stop-color="var(--red-core)"/>
        <stop offset="1" stop-color="var(--red-edge)"/>
      </linearGradient>
    </defs>

    <rect class="card-sky" width="538" height="332" fill="url(#back-sky)"/>
    <path class="trim" d="M0,299 Q269,250 538,298 L538,302 Q269,254 0,303 Z" fill="var(--cream)"/>
    <path class="card-red-base" d="M0,303 Q269,254 538,302 L538,332 L0,332 Z" fill="url(#back-red)"/>

    <circle class="brand-dot" cx="269" cy="118" r="60" fill="var(--red-edge)"/>
    <text class="brand-name" x="269" y="214" font-size="34" text-anchor="middle">JOLLY PAWS</text>
    <text class="tagline" x="270" y="240" text-anchor="middle">HAPPY DOGS, HAPPY OWNERS</text>
  </svg>

</main>
</body>
</html>
```